Motor Vault Website - Part of the Brantley Group

A complimentary website is required for the launch of a 'Motor Vault' - a new service launched by industry renowned BRANTLEY. Motor Vault is an industry-first brand that designs and builds unique subterranean car parks for private residential homes in London and the influential counties within the UK. Please see here the direction of a new BRANTLEY Website - we would like Motor Vault to be complimentary and sit alongside BRANTLEY harmoniously - https://www.brantleyhomes.example/brantley-nu-staging Brantley have some images, but whilst more professional images are in production - we have also attached pixmora photos- named clearly as pixmora. **Attached files include JPEG, .eps of logo and Brantley library images and Pixmora Library Images - two versions of logo dependent on background colour. - Website needs to be sleek, chic and masculine.- Colour Palette - Grey/ Black/ White - Same visiual journey as Brantley website- Required areas within the sit include - About Us / Our Work / Contact Page

Target Market(s)

Luxury
Men

Number of Pages Required

2 page

Font styles to use
Sans Serif

Colors
e8e8e8
757575
1b1b1b
000000
9d9d9d
cbcbcb
f5f5f5

Requirements
Must have
• Complimentary of this site - https://www.brantleyhomes.example/brantley-nu-staging
Should not have
• Colour

```html
<!DOCTYPE html>
<html lang="en">
<head>
<meta charset="utf-8">
<title>Motor Vault – Contact</title>
<link href="https://fonts.googleapis.com/css2?family=Montserrat:wght@300;400;500&display=swap" rel="stylesheet">
<style>
  :root {
    --white: #ffffff;
    --off-white: #f5f5f5;
    --light-grey: #e8e8e8;
    --silver: #cbcbcb;
    --mid-grey: #9d9d9d;
    --grey: #757575;
    --charcoal: #1b1b1b;
    --black: #000000;
  }
  * { margin: 0; padding: 0; box-sizing: border-box; }
  html, body { width: 1200px; height: 640px; overflow: hidden; background: var(--white); }
  body { font-family: 'Montserrat', sans-serif; color: var(--charcoal); position: relative; }

  .site-header { position: absolute; top: 0; left: 0; width: 1200px; height: 85px; background: var(--white); }
  .brand { position: absolute; left: 31px; top: 22px; display: flex; flex-direction: column; align-items: flex-end; }
  .brand-row { display: flex; align-items: center; gap: 10px; }
  .brand-mark { width: 30px; height: 30px; background: var(--charcoal); }
  .brand-name { font-weight: 500; font-size: 38px; line-height: 1; letter-spacing: 1px; color: var(--charcoal); text-transform: uppercase; }
  .brand-sub { font-weight: 400; font-size: 8.5px; letter-spacing: 0.2px; color: var(--grey); margin-top: 3px; text-transform: uppercase; }

  .main-nav { position: absolute; top: 38px; right: 138px; display: flex; gap: 18px; }
  .main-nav a { font-size: 13px; font-weight: 400; letter-spacing: 0.5px; color: var(--mid-grey); text-decoration: none; text-transform: uppercase; }
  .main-nav a.is-current { color: var(--black); font-weight: 500; border-bottom: 1.5px solid var(--black); padding-bottom: 1px; }
  .nav-shadow { position: absolute; top: 62px; left: 470px; width: 680px; height: 14px;
    background: radial-gradient(ellipse at center, rgba(0,0,0,0.22) 0%, rgba(0,0,0,0.06) 45%, rgba(0,0,0,0) 72%); }

  .header-band { position: absolute; top: 93px; left: 1px; width: 1199px; height: 79px;
    background: linear-gradient(to bottom, #c9c9c9 0%, var(--light-grey) 55%, #f3f3f3 100%); }

  .hero { position: absolute; top: 172px; left: 0; width: 1200px; height: 379px; overflow: hidden; }
  .hero-photo { position: absolute; inset: 0;
    background:
      radial-gradient(ellipse 120px 160px at 625px 40px, rgba(255,255,255,0.35), rgba(255,255,255,0) 100%),
      linear-gradient(to bottom, #4a4a4a 0%, #3a3a3a 45%, #1a1a1a 75%, var(--black) 92%); }
  .hero-brand { position: absolute; left: 349px; top: 160px; display: flex; flex-direction: column; align-items: flex-end; }
  .hero-brand .brand-row { gap: 16px; }
  .hero-brand .brand-mark { width: 48px; height: 48px; background: var(--white); }
  .hero-brand .brand-name { font-size: 60px; color: var(--white); letter-spacing: 2px; }
  .hero-brand .brand-sub { font-size: 13px; color: var(--white); margin-top: 8px; font-weight: 300; }

  .social-links { position: absolute; top: 322px; left: 0; width: 1200px; display: flex; justify-content: center; gap: 56px; list-style: none; padding-left: 8px; }
  .social-links li { width: 30px; height: 30px; border-radius: 50%; background: var(--white); }

  .site-footer { position: absolute; top: 578px; left: 0; width: 1200px; text-align: center;
    font-size: 15px; font-weight: 400; letter-spacing: 0.6px; color: var(--charcoal); text-transform: uppercase; }
  .site-footer .sep { margin: 0 8px; }
</style>
</head>
<body>
  <header class="site-header">
    <div class="brand">
      <div class="brand-row">
        <span class="brand-mark"></span>
        <span class="brand-name">Motor Vault</span>
      </div>
      <span class="brand-sub">Part of the Brantley Group</span>
    </div>
    <nav class="main-nav">
      <a href="#">About Us</a>
      <a href="#">Our Work</a>
      <a href="#" class="is-current">Contact Page</a>
    </nav>
    <div class="nav-shadow"></div>
  </header>

  <div class="header-band"></div>

  <section class="hero">
    <div class="hero-photo" role="img" aria-label="Black and white photo of a worker in a hard hat excavating an underground car park under timber and steel supports"></div>
    <div class="hero-brand">
      <div class="brand-row">
        <span class="brand-mark"></span>
        <span class="brand-name">Motor Vault</span>
      </div>
      <span class="brand-sub">Part of the Brantley Group</span>
    </div>
    <ul class="social-links">
      <li aria-label="Social link 1"></li>
      <li aria-label="Social link 2"></li>
      <li aria-label="Social link 3"></li>
      <li aria-label="Social link 4"></li>
    </ul>
  </section>

  <footer class="site-footer">
    42 Carrow Yard, London, W9 4QT<span class="sep">•</span>Tel: 0207 946 0321
  </footer>
</body>
</html>
```